App-Design für IT-Sicherheitsfirma
Zielgruppe
Wir sind eine IT-Sicherheitsfirma und suchen ein funktionelles und schlankes App Design.
Unsere Nutzer sind Mitarbeiter von international agierenden Konzernen. Die Zielgruppe sind international agierende Konzerne.
Die App gibt die Möglichkeit zu einem sehr sicheren Login auf Großrechner (Mainframes) via Handy oder Webinterface. Vereinfacht gesagt ist sie ein Login-Tool, Schlüssel oder Authenticator.
Aufgabenstellung
Die App soll übersichtlich, sicher, modern, schlicht und smart aussehen. Schön aber kein muss wäre die Verwendung von Elementen aus 'wirbel/gestalt' da wir die App auf dieser Plattform programmieren wollen.
https://gestaltkern.io/design/gestalt-theming/overview.html#gestalt-theming
https://wirbel.dev/docs/development/ui/widgets/gestalt

```html
<!DOCTYPE html>
<html lang="en">
<head>
<meta charset="utf-8">
<title>Legate pass – app screens</title>
<link href="https://fonts.googleapis.com/css2?family=Inter:wght@400;500;600;700&family=IBM+Plex+Mono:wght@300;400&display=swap" rel="stylesheet">
<style>
:root{
  --board:#e6e6e6;
  --note:#8a8a8a;
  --screen-top:#2c2c2c;
  --screen-top-2:#353535;
  --sheet:#1b1b1b;
  --body:#121212;
  --field:#4b4b4b;
  --card:#4a4a4a;
  --header:#2a2a2a;
  --tabbar:#333333;
  --white:#ffffff;
  --accent:#c0281e;
  --error:#c3271d;
}
*{box-sizing:border-box;margin:0;padding:0}
html,body{width:972px;height:1200px;overflow:hidden;background:var(--board)}
body{position:relative;font-family:"Inter",sans-serif;color:var(--white)}
.note{position:absolute;font-family:"IBM Plex Mono",monospace;font-weight:300;font-size:7.5px;line-height:11px;color:var(--note);white-space:nowrap}
.note.right{text-align:right}
.leaders{position:absolute;left:0;top:0;width:972px;height:1200px;pointer-events:none}
.leaders path{fill:none;stroke:var(--note);stroke-width:.6}

.phone{position:absolute;width:200px;height:432px;overflow:hidden;background:var(--sheet);box-shadow:0 4px 14px rgba(0,0,0,.12)}
.facets{position:absolute;inset:0;background:linear-gradient(155deg,var(--screen-top-2) 0%,var(--screen-top) 40%,#262626 70%,#303030 100%)}
.status{position:absolute;left:0;top:0;width:100%;height:20px}
.status .time{position:absolute;left:17px;top:7px;font-size:8px;font-weight:600}
.status .notch{position:absolute;left:44px;top:0;width:112px;height:15px;background:#000;border-radius:0 0 9px 9px}
.status svg{position:absolute;right:9px;top:8px}
.home{position:absolute;left:64px;bottom:4px;width:71px;height:2px;border-radius:2px;background:#000}
.home.light{background:#fff}

.launch-art{position:absolute;left:0;top:160px;width:120px;height:50px;background:linear-gradient(90deg,rgba(255,255,255,0) 0%,rgba(255,255,255,.06) 100%)}
.hero-title{position:absolute;left:0;width:100%;text-align:center;font-size:17.5px;font-weight:600;letter-spacing:-.1px}
.byline{position:absolute;left:0;width:100%;text-align:center;font-size:7.5px;font-weight:500}
.sheet{position:absolute;left:0;right:0;bottom:0;background:var(--sheet);border-radius:10px 10px 0 0}

.field{position:absolute;left:13px;width:173px;height:33px;background:var(--field);padding:5px 5px 0}
.field .label{font-size:7px;line-height:9px;font-weight:400}
.field .value{font-size:9.5px;line-height:13px;font-weight:600}
.field.invalid{background:#000;border:1px solid var(--error);height:48px;padding:4px 5px 0}
.field .error{position:absolute;left:0;right:0;bottom:0;height:15px;background:var(--error);font-size:7px;font-weight:400;display:flex;align-items:center;gap:4px;padding-left:5px}
.btn{position:absolute;left:13px;width:173px;height:28px;background:var(--white);color:var(--accent);font-size:9.5px;font-weight:600;display:flex;align-items:center;justify-content:center;gap:3px}

.device{position:absolute;left:13px;top:246px;width:173px;height:55px;background:var(--field);display:flex;align-items:center;padding-left:13px;gap:13px}
.device .name{font-size:9px;font-weight:600;margin-bottom:2px}
.device .spec{font-size:6.8px;font-weight:600;line-height:9px}
.link{position:absolute;left:0;width:100%;text-align:center;font-size:7.5px;font-weight:600}

.appbar{position:absolute;left:0;top:0;width:100%;height:52px;background:var(--header)}
.appbar .title{position:absolute;left:13px;top:31px;font-size:11.5px;font-weight:600}
.appbar .more{position:absolute;right:15px;top:37px;display:flex;gap:2px}
.appbar .more i{width:2.2px;height:2.2px;border-radius:50%;background:#fff;display:block}
.content{position:absolute;left:0;top:52px;width:100%;bottom:0;background:var(--body)}
.section{position:absolute;left:13px;top:80px;font-size:9px;font-weight:400;color:#e8e8e8}
.filter{position:absolute;right:13px;top:80px;font-size:7.5px;font-weight:600}

.mainframe{position:absolute;left:13px;width:173px;height:58px;background:var(--card)}
.mainframe .drive{position:absolute;left:9px;top:14px}
.mainframe .enter{position:absolute;right:8px;top:12px}
.mainframe .name{position:absolute;left:45px;top:11px;font-size:9px;font-weight:600}
.tag-code{position:absolute;left:45px;top:25px;background:#fff;color:#111;font-family:"IBM Plex Mono",monospace;font-size:7px;line-height:11px;padding:0 3px;border-radius:1.5px}
.mainframe .host{position:absolute;left:45px;top:40px;font-size:7px;color:#d6d6d6}

.request{position:absolute;left:0;width:100%;height:49px;background:var(--card);border-bottom:1px solid #3a3a3a}
.request .check{position:absolute;left:14px;top:6px}
.request .chev{position:absolute;right:14px;top:8px}
.request .name{position:absolute;left:34px;top:6px;font-size:9px;font-weight:600}
.request .date{position:absolute;left:34px;top:19px;font-size:7px}
.request .tags{position:absolute;left:34px;top:31px;display:flex;gap:2px}
.tag{background:#fff;color:#8c8c8c;font-family:"IBM Plex Mono",monospace;font-size:6.8px;line-height:11px;padding:0 3px;border-radius:1.5px}

.tabbar{position:absolute;left:0;bottom:0;width:100%;height:53px;background:var(--tabbar)}
.tab{position:absolute;top:6px;width:80px;text-align:center;font-size:8.5px;font-weight:500;color:#fff}
.tab.off{color:#7a7a7a}
.tab svg{display:block;margin:2px auto 3px}
</style>
</head>
<body>

<div class="note" style="left:133px;top:89px">Legate pass<br>for korvelt</div>
<div class="note" style="left:614px;top:89px">Background could move<br>when the phone is tilted</div>
<div class="note" style="left:44px;top:457px">Launchscreen</div>
<div class="note right" style="left:266px;top:601px;width:100px">Phone info displayed<br>more subtle here</div>
<div class="note" style="left:857px;top:339px">Example of validation<br>and error message.</div>
<div class="note" style="left:857px;top:726px">Add filter functionality?</div>
<div class="note" style="left:857px;top:817px">Drilldown instead<br>of accordeon<br>(works better on mobile)</div>
<div class="note" style="left:850px;top:974px">Tags instead of icons<br>for better readability</div>
<div class="note" style="left:281px;top:1115px">Option to reset<br>the app</div>

<!-- launch screen -->
<div class="phone" style="left:133px;top:133px;background:var(--screen-top)">
  <div class="facets" role="img" aria-label="Dark faceted geometric background"></div>
  <div class="launch-art" role="img" aria-label="Paper plane flying upward with a curved trail"></div>
  <div class="status"><span class="time">9:41</span><span class="notch"></span>
    <svg width="34" height="6" viewBox="0 0 34 6"><rect x="0" y="4" width="1.4" height="2" fill="#fff"/><rect x="2.2" y="3" width="1.4" height="3" fill="#fff"/><rect x="4.4" y="1.6" width="1.4" height="4.4" fill="#fff"/><rect x="6.6" y="0" width="1.4" height="6" fill="#fff"/><path d="M12 2.2a5 5 0 0 1 7 0M13.3 3.6a3 3 0 0 1 4.4 0" stroke="#fff" stroke-width=".9" fill="none"/><circle cx="15.5" cy="5.2" r=".8" fill="#fff"/><rect x="22" y=".5" width="10" height="5" rx="1.2" fill="#fff"/><rect x="32.5" y="2" width="1" height="2" fill="#fff"/></svg>
  </div>
  <div class="hero-title" style="top:214px">Legate pass</div>
  <div class="byline" style="top:243px">by Korvelt</div>
  <div class="home"></div>
</div>

<!-- register -->
<div class="phone" style="left:386px;top:133px">
  <div class="facets" role="img" aria-label="Dark faceted geometric background"></div>
  <div class="status"><span class="time">9:41</span><span class="notch"></span>
    <svg width="34" height="6" viewBox="0 0 34 6"><rect x="0" y="4" width="1.4" height="2" fill="#fff"/><rect x="2.2" y="3" width="1.4" height="3" fill="#fff"/><rect x="4.4" y="1.6" width="1.4" height="4.4" fill="#fff"/><rect x="6.6" y="0" width="1.4" height="6" fill="#fff"/><path d="M12 2.2a5 5 0 0 1 7 0M13.3 3.6a3 3 0 0 1 4.4 0" stroke="#fff" stroke-width=".9" fill="none"/><circle cx="15.5" cy="5.2" r=".8" fill="#fff"/><rect x="22" y=".5" width="10" height="5" rx="1.2" fill="#fff"/><rect x="32.5" y="2" width="1" height="2" fill="#fff"/></svg>
  </div>
  <div class="hero-title" style="top:113px">Legate pass</div>
  <div class="sheet" style="top:159px"></div>
  <div class="field" style="top:187px"><div class="label">E-Mail</div><div class="value">lukas.brenner@korvelt.com</div></div>
  <div class="field" style="top:228px"><div class="label">First name</div><div class="value">Lukas</div></div>
  <div class="field" style="top:269px"><div class="label">Last name</div><div class="value">Brenner</div></div>
  <div class="btn" style="top:309px">Register <span>&rarr;</span></div>
  <div class="home"></div>
</div>

<!-- register error -->
<div class="phone" style="left:641px;top:133px">
  <div class="facets" role="img" aria-label="Dark faceted geometric background"></div>
  <div class="status"><span class="time">9:41</span><span class="notch"></span>
    <svg width="34" height="6" viewBox="0 0 34 6"><rect x="0" y="4" width="1.4" height="2" fill="#fff"/><rect x="2.2" y="3" width="1.4" height="3" fill="#fff"/><rect x="4.4" y="1.6" width="1.4" height="4.4" fill="#fff"/><rect x="6.6" y="0" width="1.4" height="6" fill="#fff"/><path d="M12 2.2a5 5 0 0 1 7 0M13.3 3.6a3 3 0 0 1 4.4 0" stroke="#fff" stroke-width=".9" fill="none"/><circle cx="15.5" cy="5.2" r=".8" fill="#fff"/><rect x="22" y=".5" width="10" height="5" rx="1.2" fill="#fff"/><rect x="32.5" y="2" width="1" height="2" fill="#fff"/></svg>
  </div>
  <div class="hero-title" style="top:113px">Legate pass</div>
  <div class="sheet" style="top:159px"></div>
  <div class="field invalid" style="top:187px"><div class="label">E-Mail</div><div class="value">lukas.brenner@postwolke.com</div>
    <div class="error"><svg width="8" height="7" viewBox="0 0 8 7"><path d="M4 .5L7.5 6.5H.5Z" fill="none" stroke="#fff" stroke-width=".7"/><path d="M4 2.6v2M4 5.3v.5" stroke="#fff" stroke-width=".7"/></svg>This email is not allowed.</div></div>
  <div class="field" style="top:243px"><div class="label">First name</div><div class="value">Lukas</div></div>
  <div class="field" style="top:284px"><div class="label">Last name</div><div class="value">Brenner</div></div>
  <div class="btn" style="top:324px">Register <span>&rarr;</span></div>
  <div class="home"></div>
</div>

<!-- login -->
<div class="phone" style="left:133px;top:646px">
  <div class="facets" role="img" aria-label="Dark faceted geometric background"></div>
  <div class="status"><span class="time">9:41</span><span class="notch"></span>
    <svg width="34" height="6" viewBox="0 0 34 6"><rect x="0" y="4" width="1.4" height="2" fill="#fff"/><rect x="2.2" y="3" width="1.4" height="3" fill="#fff"/><rect x="4.4" y="1.6" width="1.4" height="4.4" fill="#fff"/><rect x="6.6" y="0" width="1.4" height="6" fill="#fff"/><path d="M12 2.2a5 5 0 0 1 7 0M13.3 3.6a3 3 0 0 1 4.4 0" stroke="#fff" stroke-width=".9" fill="none"/><circle cx="15.5" cy="5.2" r=".8" fill="#fff"/><rect x="22" y=".5" width="10" height="5" rx="1.2" fill="#fff"/><rect x="32.5" y="2" width="1" height="2" fill="#fff"/></svg>
  </div>
  <div class="hero-title" style="top:172px">Legate pass</div>
  <div class="sheet" style="top:219px"></div>
  <div class="device">
    <svg width="19" height="34" viewBox="0 0 19 34"><rect x=".5" y=".5" width="18" height="33" rx="1" fill="none" stroke="#fff" stroke-width=".8"/><path d="M7.5 30.5h4" stroke="#fff" stroke-width=".8"/></svg>
    <div><div class="name">Lukas Fone</div><div class="spec">Model: Fone X12 Pro<br>OS: MobOS 14.6</div></div>
  </div>
  <div class="btn" style="top:309px">Login <span>&rarr;</span></div>
  <div class="link" style="top:359px">Change account</div>
  <div class="home"></div>
</div>

<!-- mainframes -->
<div class="phone" style="left:386px;top:646px">
  <div class="appbar">
    <div class="status"><span class="time">9:41</span><span class="notch"></span>
      <svg width="34" height="6" viewBox="0 0 34 6"><rect x="0" y="4" width="1.4" height="2" fill="#fff"/><rect x="2.2" y="3" width="1.4" height="3" fill="#fff"/><rect x="4.4" y="1.6" width="1.4" height="4.4" fill="#fff"/><rect x="6.6" y="0" width="1.4" height="6" fill="#fff"/><path d="M12 2.2a5 5 0 0 1 7 0M13.3 3.6a3 3 0 0 1 4.4 0" stroke="#fff" stroke-width=".9" fill="none"/><circle cx="15.5" cy="5.2" r=".8" fill="#fff"/><rect x="22" y=".5" width="10" height="5" rx="1.2" fill="#fff"/><rect x="32.5" y="2" width="1" height="2" fill="#fff"/></svg>
    </div>
    <div class="title">Legate pass</div><div class="more"><i></i><i></i><i></i></div>
  </div>
  <div class="content"></div>
  <div class="section">Available mainframes</div>

  <div class="mainframe" style="top:99px">
    <svg class="drive" width="27" height="27" viewBox="0 0 27 27"><path d="M5 2h17l4 14v9H1v-9Z" fill="none" stroke="#fff" stroke-width=".8"/><path d="M1 16h25" stroke="#fff" stroke-width=".8"/><circle cx="21" cy="21" r="1.6" fill="none" stroke="#fff" stroke-width=".8"/></svg>
    <div class="name">Korvelt Demo</div><div class="tag-code">qsh</div><div class="host">mainframe.dev-korvelt.com</div>
    <svg class="enter" width="10" height="10" viewBox="0 0 10 10"><path d="M6 .5h3.5v9H6M.5 5h6M4.5 3l2 2-2 2" fill="none" stroke="#fff" stroke-width=".8"/></svg>
  </div>
  <div class="mainframe" style="top:166px">
    <svg class="drive" width="27" height="27" viewBox="0 0 27 27"><path d="M5 2h17l4 14v9H1v-9Z" fill="none" stroke="#fff" stroke-width=".8"/><path d="M1 16h25" stroke="#fff" stroke-width=".8"/><circle cx="21" cy="21" r="1.6" fill="none" stroke="#fff" stroke-width=".8"/></svg>
    <div class="name">Korvelt Test</div><div class="tag-code">kacl</div><div class="host">mainframe.dev-korvelt.com</div>
    <svg class="enter" width="10" height="10" viewBox="0 0 10 10"><path d="M6 .5h3.5v9H6M.5 5h6M4.5 3l2 2-2 2" fill="none" stroke="#fff" stroke-width=".8"/></svg>
  </div>
  <div class="mainframe" style="top:233px">
    <svg class="drive" width="27" height="27" viewBox="0 0 27 27"><path d="M5 2h17l4 14v9H1v-9Z" fill="none" stroke="#fff" stroke-width=".8"/><path d="M1 16h25" stroke="#fff" stroke-width=".8"/><circle cx="21" cy="21" r="1.6" fill="none" stroke="#fff" stroke-width=".8"/></svg>
    <div class="name">Korvelt Trial</div><div class="tag-code">virtual setup</div><div class="host">mainframe.dev-korvelt.com</div>
    <svg class="enter" width="10" height="10" viewBox="0 0 10 10"><path d="M6 .5h3.5v9H6M.5 5h6M4.5 3l2 2-2 2" fill="none" stroke="#fff" stroke-width=".8"/></svg>
  </div>

  <div class="tabbar">
    <div class="tab" style="left:20px"><svg width="11" height="10" viewBox="0 0 11 10"><path d="M1 1.5h9M1 4h6M1 6.5h9M1 9h5" stroke="#fff" stroke-width=".9"/></svg>Terminal</div>
    <div class="tab off" style="left:100px"><svg width="12" height="11" viewBox="0 0 12 11"><path d="M2.2 5.5a4.3 4.3 0 1 1 1.3 3.1M2.2 5.5L1 4.2M2.2 5.5l1.3-1.2M7 3v2.8l1.8 1.2" fill="none" stroke="#7a7a7a" stroke-width=".9"/></svg>Logins</div>
    <div class="home light"></div>
  </div>
</div>

<!-- logins -->
<div class="phone" style="left:639px;top:646px">
  <div class="appbar">
    <div class="status"><span class="time">9:41</span><span class="notch"></span>
      <svg width="34" height="6" viewBox="0 0 34 6"><rect x="0" y="4" width="1.4" height="2" fill="#fff"/><rect x="2.2" y="3" width="1.4" height="3" fill="#fff"/><rect x="4.4" y="1.6" width="1.4" height="4.4" fill="#fff"/><rect x="6.6" y="0" width="1.4" height="6" fill="#fff"/><path d="M12 2.2a5 5 0 0 1 7 0M13.3 3.6a3 3 0 0 1 4.4 0" stroke="#fff" stroke-width=".9" fill="none"/><circle cx="15.5" cy="5.2" r=".8" fill="#fff"/><rect x="22" y=".5" width="10" height="5" rx="1.2" fill="#fff"/><rect x="32.5" y="2" width="1" height="2" fill="#fff"/></svg>
    </div>
    <div class="title">Legate pass</div><div class="more"><i></i><i></i><i></i></div>
  </div>
  <div class="content"></div>
  <div class="section">Authentication requests</div>
  <div class="filter">Filter list</div>

  <div class="request" style="top:99px">
    <svg class="check" width="13" height="13" viewBox="0 0 13 13"><circle cx="6.5" cy="6.5" r="6" fill="none" stroke="#fff" stroke-width=".8"/><path d="M3.8 6.7l1.9 1.9 3.6-3.8" fill="none" stroke="#fff" stroke-width=".8"/></svg>
    <div class="name">Lukas Brenner</div><div class="date">23.07.2021, 20:00:00</div>
    <div class="tags"><span class="tag">2FA</span><span class="tag">FingerID</span></div>
    <svg class="chev" width="6" height="10" viewBox="0 0 6 10"><path d="M1 1l4 4-4 4" fill="none" stroke="#fff" stroke-width=".9"/></svg>
  </div>
  <div class="request" style="top:149px">
    <svg class="check" width="13" height="13" viewBox="0 0 13 13"><circle cx="6.5" cy="6.5" r="6" fill="none" stroke="#fff" stroke-width=".8"/><path d="M3.8 6.7l1.9 1.9 3.6-3.8" fill="none" stroke="#fff" stroke-width=".8"/></svg>
    <div class="name">Lukas Brenner</div><div class="date">23.07.2021, 16:20:00</div>
    <div class="tags"><span class="tag">2FA</span><span class="tag">FingerID</span></div>
    <svg class="chev" width="6" height="10" viewBox="0 0 6 10"><path d="M1 1l4 4-4 4" fill="none" stroke="#fff" stroke-width=".9"/></svg>
  </div>
  <div class="request" style="top:199px">
    <svg class="check" width="13" height="13" viewBox="0 0 13 13"><circle cx="6.5" cy="6.5" r="6" fill="none" stroke="#fff" stroke-width=".8"/><path d="M3.8 6.7l1.9 1.9 3.6-3.8" fill="none" stroke="#fff" stroke-width=".8"/></svg>
    <div class="name">Lukas Brenner</div><div class="date">23.07.2021, 08:15:45</div>
    <div class="tags"><span class="tag">Accesstoken</span></div>
    <svg class="chev" width="6" height="10" viewBox="0 0 6 10"><path d="M1 1l4 4-4 4" fill="none" stroke="#fff" stroke-width=".9"/></svg>
  </div>
  <div class="request" style="top:249px;border-bottom:0">
    <svg class="check" width="13" height="13" viewBox="0 0 13 13"><circle cx="6.5" cy="6.5" r="6" fill="none" stroke="#fff" stroke-width=".8"/><path d="M3.8 6.7l1.9 1.9 3.6-3.8" fill="none" stroke="#fff" stroke-width=".8"/></svg>
    <div class="name">Lukas Brenner</div><div class="date">Yesterday, 23.07.2021, 23:52:56</div>
    <div class="tags"><span class="tag">2FA</span><span class="tag">FingerID</span></div>
    <svg class="chev" width="6" height="10" viewBox="0 0 6 10"><path d="M1 1l4 4-4 4" fill="none" stroke="#fff" stroke-width=".9"/></svg>
  </div>

  <div class="tabbar">
    <div class="tab off" style="left:20px"><svg width="11" height="10" viewBox="0 0 11 10"><path d="M1 1.5h9M1 4h6M1 6.5h9M1 9h5" stroke="#7a7a7a" stroke-width=".9"/></svg>Terminal</div>
    <div class="tab" style="left:100px"><svg width="12" height="11" viewBox="0 0 12 11"><path d="M2.2 5.5a4.3 4.3 0 1 1 1.3 3.1M2.2 5.5L1 4.2M2.2 5.5l1.3-1.2M7 3v2.8l1.8 1.2" fill="none" stroke="#fff" stroke-width=".9"/></svg>Logins</div>
    <div class="home light"></div>
  </div>
</div>

<svg class="leaders" viewBox="0 0 972 1200">
  <path d="M607 104C580 110 560 130 552 164M549 160l3 4 2-5"/>
  <path d="M101 462C120 460 145 458 157 451M153 449l4 2-3 3"/>
  <path d="M371 605C410 590 440 560 454 507M451 511l3-4 2 5"/>
  <path d="M851 344H834M837 342l-3 2 3 2"/>
  <path d="M851 731H834M837 729l-3 2 3 2"/>
  <path d="M851 823C838 826 832 838 830 850"/>
  <path d="M844 980C790 980 760 975 735 941M734 945l1-4 3 2"/>
  <path d="M275 1121C245 1118 236 1085 233 1045M231 1049l2-4 2 4"/>
</svg>
</body>
</html>
```